Design a DL flyer double sided 4 colour 210mm x 95 mm (portrait) for the launch of a new yoga studio opening in North Melbourne on the 23 November 2013.
The final design should communicate with a strong call to action- the opening date , register to receive your first class free and like us on Chatterbox.
The studio provides a tranquil, open space to practice yoga, create a feeling of light, peace and a nurturing environment, please create this feeling in the design.

An example design mock (rough design feel free to move around as required, includes final content) print specifications, logo, typography style and image attached.
The reverse side to include logo, address and please design the timetable for the launch week (refer design mock)
Have also attached a reverse logo for a dark background and are open to designer providing examples with various background colours and effects.
Back content can be moved to the front side if required to facilitate design

Target Market(s)

People in the area who are practicing yoga elsewhere and encourage them to come to the studio to try us out with a free opening offer in our first week. And people new to yoga wanting to give it a try.
Experienced yoga people and people new to yoga - all ages

Industry/Entity Type

Environment

Requirements
Must have
• The Lotus Nook logo physical address, website address, the tagline live, breathe, love...
The final design should communicate with a strong call to action- the opening date , register to receive your first class free and like us on Chatterbox. and the website address thelotusnook.com.au, drive them to the website to register.
The studio provides a tranquil, open space to practice yoga, create a feeling of light, peace and a nurturing environment, please create this feeling in the design

```html
<!DOCTYPE html>
<html lang="en">
<head>
<meta charset="utf-8">
<title>The Lotus Nook – DL Flyer</title>
<link href="https://fonts.googleapis.com/css2?family=Great+Vibes&family=Roboto+Condensed:wght@300;400;700&display=swap" rel="stylesheet">
<style>
:root{
  --stage:#d5d5d7;
  --floor:#ffffff;
  --orange:#f08a1c;
  --orange-soft:#f8ad3e;
  --orange-pale:#fbd9a8;
  --earth:#6e6253;
  --earth-dark:#5a4f42;
  --ink:#555049;
  --paper:#ffffff;
  --table-bg:#e9e3d7;
  --table-line:#a59c8d;
}
*{margin:0;padding:0;box-sizing:border-box}
html,body{width:1200px;height:1152px;overflow:hidden}
body{background:var(--stage);font-family:"Roboto Condensed",Arial,sans-serif;position:relative}
.floor{position:absolute;left:0;top:1145px;width:1200px;height:7px;background:var(--floor)}
.flyer{position:absolute;top:85px;width:484px;height:989px;overflow:hidden;box-shadow:8px 8px 14px rgba(0,0,0,.28)}
.flyer--front{left:65px;background:var(--paper)}
.flyer--back{left:638px;background:var(--earth)}

.brand{position:absolute;top:48px;left:0;width:100%;text-align:center}
.brand__name{display:inline-flex;align-items:center;gap:10px;font-size:30px;font-weight:400;letter-spacing:.5px}
.brand__dot{width:22px;height:22px;border-radius:50%;background:var(--orange)}
.brand__tagline{font-size:15px;margin-top:6px}
.brand__address{font-size:12.5px;margin-top:5px;letter-spacing:.2px}
.flyer--front .brand{color:var(--ink)}
.flyer--front .brand__name{color:var(--ink)}
.flyer--back .brand,.flyer--back .brand__name{color:#fff}

.front__glow{position:absolute;left:0;top:0;width:100%;height:100%}
.front__photo{position:absolute;left:0;top:410px;width:484px;height:500px;
  background:radial-gradient(ellipse at 45% 30%,#eef0d8 0%,#a9bf7a 25%,#4f7436 55%,#2d4224 85%)}
.headline{position:absolute;top:138px;width:100%;text-align:center;font-family:"Great Vibes",cursive;font-size:58px;color:var(--ink);font-weight:400}
.offer{position:absolute;top:214px;width:100%;text-align:center;color:var(--orange);font-size:19.5px;line-height:23px}
.details{position:absolute;top:283px;left:53px;width:390px;color:var(--ink);font-size:15.5px;line-height:19.5px}
.front__url{position:absolute;top:946px;width:100%;text-align:center;color:#fff;font-size:16px}

.back__photo{float:left;width:211px;height:149px;margin:0 18px 6px 0;border-radius:6px;
  background:radial-gradient(ellipse at 70% 45%,#f2e6d6 0%,#d9a979 30%,#9c6b3b 55%,#5e6e2c 85%)}
.intro{position:absolute;top:156px;left:43px;width:399px;color:#fff;font-size:18px;line-height:21.3px;text-align:justify;font-weight:300}
.intro p{margin-bottom:21px}

.timetable{position:absolute;top:581px;left:43px;width:399px}
.timetable__title{height:38px;background:var(--orange-soft);color:#fff;font-weight:700;font-size:18px;text-align:center;line-height:38px}
.timetable table{width:100%;border-collapse:collapse;background:var(--table-bg);color:var(--ink);font-size:11.5px;table-layout:fixed}
.timetable th{font-weight:400;text-align:left;padding:3px 4px;border-left:1px solid #fff;border-bottom:1px solid var(--table-line);height:20px}
.timetable td{padding:0 4px;height:18px;border-left:1px solid #fff;border-bottom:1px dashed var(--table-line)}
.timetable th:first-child,.timetable td:first-child{border-left:none}

.back__band{position:absolute;left:0;top:700px;width:100%;height:289px}
.hours{position:absolute;top:829px;width:100%;text-align:center;color:#fff;font-weight:700;font-size:18px;letter-spacing:.3px}
.contact{position:absolute;top:868px;left:43px;color:#fff;font-size:16.5px;line-height:19.5px;list-style:none}
.contact li{display:flex;gap:7px;align-items:flex-start}
.contact svg{width:13px;height:13px;margin-top:3px;flex:none}
.contact .indent{padding-left:20px}
.findus{position:absolute;top:868px;left:298px;color:#fff;font-size:16.5px}
.findus__map{width:144px;height:72px;margin-top:2px;border-radius:3px;background:linear-gradient(135deg,#ece7da,#f4efe2 50%,#dcd6c6)}
</style>
</head>
<body>

<section class="flyer flyer--front">
  <svg class="front__glow" viewBox="0 0 484 989" aria-hidden="true">
    <defs>
      <linearGradient id="warm" x1="0" y1="0" x2="0" y2="1">
        <stop offset="0" stop-color="#fff"/>
        <stop offset=".22" stop-color="#fff"/>
        <stop offset=".36" stop-color="#fbd3a0"/>
        <stop offset=".46" stop-color="#f3951f"/>
        <stop offset=".52" stop-color="#d08a3e"/>
        <stop offset="1" stop-color="#6e6253"/>
      </linearGradient>
      <linearGradient id="foot" x1="0" y1="0" x2="0" y2="1">
        <stop offset="0" stop-color="#f3a64a"/>
        <stop offset=".45" stop-color="#f7c98e"/>
        <stop offset="1" stop-color="#6e6253"/>
      </linearGradient>
    </defs>
    <rect width="484" height="989" fill="url(#warm)"/>
    <path d="M0 350 C120 420 300 450 484 440" stroke="#fff" stroke-width="1.5" fill="none"/>
  </svg>
  <div class="front__photo" role="img" aria-label="Woman meditating cross-legged in a sunlit rainforest"></div>
  <svg style="position:absolute;left:0;top:840px" width="484" height="149" viewBox="0 0 484 149" aria-hidden="true">
    <path d="M0 40 C150 20 330 30 484 60 L484 149 L0 149Z" fill="url(#foot)"/>
    <path d="M0 45 C180 30 360 60 440 149" stroke="#fff" stroke-width="1.5" fill="none"/>
  </svg>

  <header class="brand">
    <div class="brand__name"><span class="brand__dot"></span>The Lotus Nook</div>
    <p class="brand__tagline">Live, breathe, love...</p>
    <p class="brand__address">118 ALDER LANE, NORTH MELBOURNE</p>
  </header>
  <h1 class="headline">New Yoga Studio</h1>
  <p class="offer">Opening 23 November<br>First class free in opening week *</p>
  <p class="details">*Opening week 23 Nov – 29 Nov inclusive<br>To book your free class go online to register and book, like us on Chatterbox The Lotus Nook - Melbourne and tell your friends.<br>View other opening specials at thelotusnook.com.au</p>
  <p class="front__url">www.thelotusnook.com.au</p>
</section>

<section class="flyer flyer--back">
  <header class="brand">
    <div class="brand__name"><span class="brand__dot"></span>The Lotus Nook</div>
    <p class="brand__tagline">Live, breathe, love...</p>
    <p class="brand__address">118 ALDER LANE, NORTH MELBOURNE</p>
  </header>

  <div class="intro">
    <div class="back__photo" role="img" aria-label="Close-up of hands resting in a meditation mudra"></div>
    <p>A generously sized natural studio in North Melbourne, providing dynamic flow vinyasa and restorative yoga for all levels from new-bies to experienced, with a collection of the best teachers.</p>
    <p>Embark on a journey to happiness within yourself – be healthy in your body and mind.</p>
    <p>Science is finally proving what yogis have known all along.... yoga is good for you!</p>
    <p>A tranquil space to de stress, build strength and healing in our bodies through our own tapas (internal heat).</p>
  </div>

  <svg class="back__band" viewBox="0 0 484 289" aria-hidden="true">
    <defs>
      <linearGradient id="band" x1="0" y1="0" x2="0" y2="1">
        <stop offset="0" stop-color="#6e6253"/>
        <stop offset=".3" stop-color="#c88a45"/>
        <stop offset=".45" stop-color="#f7c58a"/>
        <stop offset=".6" stop-color="#f3a240"/>
        <stop offset="1" stop-color="#ef8d1e"/>
      </linearGradient>
    </defs>
    <path d="M0 120 C160 80 330 70 484 95 L484 289 L0 289Z" fill="url(#band)"/>
    <g fill="#fde3b8" opacity=".35">
      <circle cx="30" cy="100" r="22"/><circle cx="110" cy="85" r="30"/><circle cx="190" cy="95" r="14"/>
      <circle cx="285" cy="80" r="18"/><circle cx="340" cy="110" r="26"/><circle cx="430" cy="80" r="34"/>
      <circle cx="60" cy="35" r="10"/><circle cx="250" cy="50" r="8"/><circle cx="470" cy="45" r="6"/>
    </g>
  </svg>

  <div class="timetable">
    <div class="timetable__title">CLASS TIMES</div>
    <table>
      <thead><tr><th>Sat</th><th>Sun</th><th>Mon</th><th>Tue</th><th>Wed</th><th>Thu</th><th>Fri</th></tr></thead>
      <tbody>
        <tr><td>9:00 AM</td><td>9:00 AM</td><td>6.30AM</td><td>6.30AM</td><td>6.30AM</td><td>6.30AM</td><td>6.30AM</td></tr>
        <tr><td>10.30 AM</td><td>10.30 AM</td><td>9.30AM</td><td>9.30AM</td><td>9.30AM</td><td>9.30AM</td><td>9.30AM</td></tr>
        <tr><td>4PM</td><td>4PM</td><td>12.30PM</td><td>12.30PM</td><td>12.30PM</td><td>12.30PM</td><td>12.30PM</td></tr>
        <tr><td></td><td></td><td>5.30PM</td><td>5.30PM</td><td>5.30PM</td><td>5.30PM</td><td>5.30PM</td></tr>
        <tr><td></td><td></td><td>7PM</td><td>7PM</td><td>7PM</td><td>7PM</td><td>7PM</td></tr>
      </tbody>
    </table>
  </div>

  <p class="hours">OPENING HOURS: OPEN SEVEN DAYS</p>
  <ul class="contact">
    <li><svg viewBox="0 0 12 12"><path d="M6 0a4 4 0 0 0-4 4c0 3 4 8 4 8s4-5 4-8a4 4 0 0 0-4-4zm0 5.5A1.5 1.5 0 1 1 6 2.5a1.5 1.5 0 0 1 0 3z" fill="#fff"/></svg>118 Alder Lane,</li>
    <li class="indent">North Melbourne Vic 3003</li>
    <li><svg viewBox="0 0 12 12"><rect x="0.5" y="2.5" width="11" height="8" fill="none" stroke="#fff"/><path d="M1 3l5 4 5-4" fill="none" stroke="#fff"/></svg>yoga@thelotusnook.com.au</li>
    <li><svg viewBox="0 0 12 12"><path d="M2 1l2 0 1 3-1.5 1a7 7 0 0 0 3.5 3.5L8 7l3 1v2c0 1-1 1.5-2 1.5C5 11 1 7 .5 3 .5 2 1 1 2 1z" fill="#fff"/></svg>0400 - 555018</li>
    <li><svg viewBox="0 0 12 12"><circle cx="6" cy="6" r="5.3" fill="none" stroke="#fff"/><path d="M.7 6h10.6M6 .7c-3 3-3 7.6 0 10.6M6 .7c3 3 3 7.6 0 10.6" fill="none" stroke="#fff" stroke-width=".8"/></svg>thelotusnook.com.au</li>
  </ul>
  <div class="findus">Find us:
    <div class="findus__map" role="img" aria-label="Street map showing the studio location in North Melbourne"></div>
  </div>
</section>

<div class="floor"></div>
</body>
</html>
```